Vault Keystone Password Manager WebApp Design

Vault Keystone is seeking an expert UI designer to provide a fresh and modern visual appeal for our product. Our inspiration comes from two major tools that have successfully managed to balance functionality and design aesthetics - Nimbus Locker and KeyHaven. We want our application to exude a similar trustworthiness and modernity, through a clean, intuitive and responsive design.
We have established preliminary mockups and would like the designer to work within these parameters while enhancing the overall user experience. The primary tasks will involve innovative and improved designs of the login screen and the password screen, both being crucial touchpoints for our users. The login screen also serves a crucial role in demonstrating how our system works.
Key Elements:
Logo Integration: We are providing the logo for Vault Keystone. The design should align with the logo, both in terms of colors and overall aesthetic, to ensure a cohesive brand identity.
Color Palette: The UI design should adhere to the color palette derived from the logo to maintain brand consistency. The design should effectively utilize these colors to highlight important elements and improve user engagement.
Trustworthy and Modern Design: The UI should be professional and trustworthy. It should mirror the look and feel of Nimbus Locker's simplicity and KeyHaven's solid security design, which inspires user confidence.
Adherence to Mockup Boundaries: The existing mockups serve as a guideline for the layout and placement of elements. The design should respect these boundaries while bringing innovation and visual appeal.
Improved Login Screen: The login screen is a key part of the user's journey and should be designed with utmost care. It should be intuitive, easy-to-use, visually engaging, and educative, showcasing how the system operates and encouraging users to sign in with confidence.
Enhanced Password Screen: The password screen, another key user touchpoint, needs improvement. The different types of passwords should be made more visible and intuitive, easing user interaction and enhancing the overall experience.
Prospective designers are encouraged to test our current version available for free at app.vaultkeystone-example.net to understand the product better and contribute to meaningful design enhancements.
The goal of this project is to provide a visually compelling and user-friendly interface for Vault Keystone that inspires user trust, while adhering to the branding elements, including color scheme and logo design. The ideal designer will have a proven track record of creating compelling UI designs that enhance user experience and engagement.
We preferred the design to be in Figma.
Please provide the 3 design so we can evaluate if we like to choice you:
1. Login Page.
2. Passwords View design
3. Single Passwod Page
We need all the pages to be design that are provided as screenshots.
Target Market(s)
Companies
Industry/Entity Type
Security,
Number of Pages Required
5+ page
Font styles to use
Look and feel
Each slider illustrates characteristics of the customer's brand and the style your logo design should communicate.

```html
<!DOCTYPE html>
<html lang="en">
<head>
<meta charset="utf-8">
<title>Vault Keystone – Overview</title>
<link rel="stylesheet" href="https://fonts.googleapis.com/css2?family=Figtree:wght@400;500;600&display=swap">
<style>
:root{
  --ink:#0d121e;
  --rail:#0c111d;
  --side:#0e1321;
  --side-line:#1d2433;
  --side-text:#d7dbe4;
  --active-bg:#1a2a4c;
  --blue:#2e6ae0;
  --blue-text:#4d8af0;
  --text:#101318;
  --muted:#8e939c;
  --line:#e6e9ef;
  --search:#f2f6fd;
  --green-bg:#ebfbef;--green:#5aa570;--green-tab:#a8ebc3;--green-ic:#cfeed8;
  --yellow-bg:#fff8e6;--yellow:#b49a4e;--yellow-tab:#fbe3a2;--yellow-ic:#fbe9b2;
  --blue-bg:#edf3ff;--blue-f:#2f64d6;--blue-tab:#c8d8fb;--blue-ic:#d4e1fb;
  --red-bg:#fff1ef;--red:#e2574c;--red-tab:#f9cbc4;--red-ic:#fbd8d3;
  --pink-bg:#fdebf5;--pink:#b7669a;--pink-tab:#f3bedc;--pink-ic:#f6cde4;
  --cyan-bg:#ebfafd;--cyan:#5aa3b3;--cyan-tab:#bdeaf3;--cyan-ic:#c9eff6;
  --grey-bg:#f5f5f6;--grey:#4f545c;--grey-tab:#cfd1d5;--grey-ic:#e3e4e7;
}
*{box-sizing:border-box;margin:0;padding:0}
html,body{width:1200px;height:750px;overflow:hidden}
body{font-family:"Figtree",sans-serif;background:#fff;color:var(--text);position:relative}
svg{display:block}
.rail{position:absolute;left:0;top:0;width:53px;height:750px;background:var(--rail);border-right:1px solid var(--side-line)}
.rail .brand-mark{position:absolute;left:13px;top:15px;width:26px;height:26px;border-radius:5px;background:var(--blue)}
.rail-item{position:absolute;left:0;width:53px;text-align:center;font-size:8.5px;color:#c6cbd5}
.rail-item svg{margin:0 auto 4px}
.rail-item.active{color:var(--blue-text)}
.rail-item.active::before{content:"";position:absolute;left:0;top:-11px;width:3px;height:45px;background:var(--blue);border-radius:0 3px 3px 0}
.rail-divider{position:absolute;left:6px;top:355px;width:41px;height:1px;background:#2a3140}
.rail .logout{position:absolute;left:17px;top:713px}
.sidebar{position:absolute;left:53px;top:0;width:200px;height:750px;background:var(--side)}
.app-name{position:absolute;left:12px;top:18px;font-size:15.5px;color:#fff;font-weight:400}
.nav{position:absolute;left:14px;top:105px;width:173px;list-style:none}
.nav li{display:flex;align-items:center;gap:10px;height:40px;padding-left:9px;font-size:12.5px;color:var(--side-text);margin-bottom:0}
.nav li.active{background:var(--active-bg);color:var(--blue-text);border-radius:8px}
.nav li svg{flex:none}
.side-divider{position:absolute;left:14px;top:471px;width:174px;height:1px;background:#262d3c}
.plan{position:absolute;left:14px;top:555px;width:173px;height:181px;background:#1b2232;border-radius:9px;overflow:hidden}
.plan-art{position:absolute;left:10px;top:-42px;width:150px;height:120px;border-radius:10px;background:linear-gradient(135deg,#3a86f5 0%,#2a4ea8 55%,#f2a32a 100%);opacity:.85}
.plan-gem{position:absolute;left:13px;top:35px;width:27px;height:27px;border-radius:50%;background:#262e40;display:flex;align-items:center;justify-content:center}
.plan-label{position:absolute;left:13px;top:63px;font-size:10.5px;color:#5c8ee8}
.plan-name{position:absolute;left:13px;top:78px;font-size:12.5px;color:#e8ebf0}
.plan-bar{position:absolute;left:13px;top:99px;width:148px;height:3px;background:#0c111c;border-radius:2px}
.plan-bar span{display:block;width:111px;height:3px;border-radius:2px;background:linear-gradient(90deg,#f4b53d,#e35b4a 35%,#3cb878 65%,#3b7ff0)}
.plan-day{position:absolute;left:13px;top:107px;font-size:8.5px;color:#9aa1ad}
.upgrade{position:absolute;left:13px;top:135px;width:147px;height:33px;border-radius:5px;background:var(--blue);color:#fff;font-size:12px;display:flex;align-items:center;justify-content:center}
.topbar{position:absolute;left:253px;top:0;width:947px;height:60px;border-bottom:1px solid var(--line)}
.search{position:absolute;left:34px;top:12px;width:655px;height:39px;background:var(--search);border-radius:8px;display:flex;align-items:center;padding-left:14px;gap:9px;font-size:10.5px;color:#b4c5e2}
.search .filter{position:absolute;right:14px;top:11px}
.bell{position:absolute;left:855px;top:21px}
.me{position:absolute;left:900px;top:17px;width:27px;height:27px;border-radius:50%;background:#c98a5a}
.section-title{position:absolute;left:287px;font-size:16px;font-weight:600}
.card{position:absolute;width:205px;height:109px;border:1px solid var(--line);border-radius:8px;background:#fff}
.card .tag{position:absolute;left:8px;top:8px;display:flex;align-items:center;gap:6px;font-size:10px;color:var(--muted)}
.tag i{width:18px;height:18px;border-radius:5px;display:flex;align-items:center;justify-content:center}
.card .more{position:absolute;right:14px;top:16px}
.card h3{position:absolute;left:8px;top:37px;font-size:14px;font-weight:600}
.card p{position:absolute;left:8px;top:58px;font-size:10px;color:var(--muted)}
.avatars{position:absolute;right:8px;bottom:8px;display:flex}
.avatars b{width:20px;height:20px;border-radius:50%;border:1.5px solid #fff;margin-left:-7px}
.avatars em{font-style:normal;width:20px;height:20px;border-radius:50%;background:#e9f8ee;color:#2f8a51;font-size:8px;display:flex;align-items:center;justify-content:center;margin-left:3px}
.folder{position:absolute;width:205px;height:108px;border-radius:8px}
.folder::before{content:"";position:absolute;left:56px;right:0;top:0;height:14px;border-radius:8px 8px 0 0;background:var(--tab);clip-path:polygon(0 0,100% 0,100% 100%,8px 100%)}
.folder::after{content:"";position:absolute;left:64px;right:5px;top:5px;height:9px;border-radius:4px 4px 0 0;background:#fff}
.folder .body{position:absolute;left:0;right:0;top:12px;bottom:0;background:var(--bg);border-radius:8px}
.folder .ic{position:absolute;left:15px;top:22px;width:31px;height:31px;border-radius:50%;background:var(--ic);display:flex;align-items:center;justify-content:center;z-index:1}
.folder .dots{position:absolute;right:19px;top:23px;width:20px;height:19px;border-radius:4px;background:var(--ic);display:flex;align-items:center;justify-content:center;z-index:1}
.folder h3{position:absolute;left:14px;top:69px;font-size:14px;font-weight:600;color:var(--c);z-index:1}
.folder p{position:absolute;left:14px;top:88px;font-size:8.5px;color:var(--c);z-index:1}
.folder .avatars{bottom:6px;z-index:1}
.green{--bg:var(--green-bg);--c:var(--green);--tab:var(--green-tab);--ic:var(--green-ic)}
.yellow{--bg:var(--yellow-bg);--c:var(--yellow);--tab:var(--yellow-tab);--ic:var(--yellow-ic)}
.bluef{--bg:var(--blue-bg);--c:var(--blue-f);--tab:var(--blue-tab);--ic:var(--blue-ic)}
.red{--bg:var(--red-bg);--c:var(--red);--tab:var(--red-tab);--ic:var(--red-ic)}
.pink{--bg:var(--pink-bg);--c:var(--pink);--tab:var(--pink-tab);--ic:var(--pink-ic)}
.cyan{--bg:var(--cyan-bg);--c:var(--cyan);--tab:var(--cyan-tab);--ic:var(--cyan-ic)}
.grey{--bg:var(--grey-bg);--c:var(--grey);--tab:var(--grey-tab);--ic:var(--grey-ic)}
.btn-new{position:absolute;left:964px;top:288px;width:98px;height:33px;border-radius:5px;background:var(--blue);color:#fff;font-size:12px;display:flex;align-items:center;justify-content:center}
.sort{position:absolute;left:1081px;top:288px;width:85px;height:32px;border:1px solid var(--line);border-radius:5px;background:#f7f8fa;font-size:10.5px;color:#555b64;display:flex;align-items:center;justify-content:center;gap:10px}
.c1{left:287px}.c2{left:512px}.c3{left:737px}.c4{left:962px}
</style>
</head>
<body>

<aside class="rail">
  <div class="brand-mark"></div>
  <div class="rail-item active" style="top:117px">
    <svg width="15" height="15" viewBox="0 0 15 15" fill="#3b7ff0"><rect x="0" y="0" width="6.5" height="6.5" rx="1.5"/><rect x="8.5" y="0" width="6.5" height="6.5" rx="1.5"/><rect x="0" y="8.5" width="6.5" height="6.5" rx="1.5"/><rect x="8.5" y="8.5" width="6.5" height="6.5" rx="1.5"/></svg>General</div>
  <div class="rail-item" style="top:164px">
    <svg width="17" height="16" viewBox="0 0 17 16" fill="none" stroke="#c6cbd5" stroke-width="1.3"><circle cx="7" cy="4.5" r="3"/><path d="M1.5 15c0-3 2.5-5 5.5-5s5.5 2 5.5 5"/><path d="M11 2a3 3 0 010 5.5M14 10c1.3.8 2 2.5 2 5"/></svg>Teams</div>
  <div class="rail-item" style="top:211px">
    <svg width="16" height="16" viewBox="0 0 16 16" fill="none" stroke="#c6cbd5" stroke-width="1.3"><path d="M10 1l1.3 3.2L14.5 5.5 11.3 6.8 10 10 8.7 6.8 5.5 5.5 8.7 4.2z"/><path d="M4 10l.8 1.7L6.5 12.5 4.8 13.3 4 15 3.2 13.3 1.5 12.5 3.2 11.7z"/></svg>Generate</div>
  <div class="rail-item" style="top:258px">
    <svg width="17" height="16" viewBox="0 0 17 16" fill="none" stroke="#c6cbd5" stroke-width="1.3"><rect x="1" y="1" width="15" height="10" rx="2"/><path d="M8.5 11v4M5.5 15h6M5 8V6M8.5 8V4M12 8V5.5"/></svg>Overview</div>
  <div class="rail-item" style="top:304px">
    <svg width="16" height="16" viewBox="0 0 16 16" fill="none" stroke="#c6cbd5" stroke-width="1.3"><circle cx="8" cy="8" r="7"/><circle cx="8" cy="8" r="2.5"/></svg>Settings</div>
  <div class="rail-divider"></div>
  <div class="rail-item" style="top:375px">
    <svg width="16" height="16" viewBox="0 0 16 16" fill="none" stroke="#c6cbd5" stroke-width="1.3"><path d="M2 10V8a6 6 0 0112 0v2"/><path d="M2 10h2.5v4H3a1 1 0 01-1-1zM14 10h-2.5v4H13a1 1 0 001-1z"/></svg>Support</div>
  <svg class="logout" width="18" height="17" viewBox="0 0 18 17" fill="none" stroke="#c6cbd5" stroke-width="1.4"><path d="M10 1H3a1.5 1.5 0 00-1.5 1.5v12A1.5 1.5 0 003 16h7"/><path d="M7 8.5h10M13.5 5l3.5 3.5-3.5 3.5"/></svg>
</aside>

<nav class="sidebar">
  <div class="app-name">Vault Keystone</div>
  <ul class="nav">
    <li class="active"><svg width="14" height="14" viewBox="0 0 14 14"><rect width="14" height="14" rx="3" fill="#3b7ff0"/><path d="M4 4.5h6M4 7h6M4 9.5h6" stroke="#1a2a4c" stroke-width="1.2"/></svg>Overview</li>
    <li><svg width="16" height="14" viewBox="0 0 16 14" fill="none" stroke="#d7dbe4" stroke-width="1.2"><circle cx="6" cy="4" r="2.8"/><path d="M1 13c0-3 2.2-4.5 5-4.5s5 1.5 5 4.5"/><path d="M10.5 1.5a2.6 2.6 0 010 5M12.5 9c1.5.6 2.5 2 2.5 4"/></svg>Shared with me</li>
    <li><svg width="14" height="15" viewBox="0 0 14 15" fill="none" stroke="#d7dbe4" stroke-width="1.2"><path d="M8 1H3a2 2 0 00-2 2v9a2 2 0 002 2h3M8 1l4 4v2"/><circle cx="10" cy="11" r="2.5"/><path d="M10 9V8"/></svg>Encrypted files</li>
    <li><svg width="14" height="13" viewBox="0 0 14 13" fill="none" stroke="#d7dbe4" stroke-width="1.2"><rect x="1" y="3" width="12" height="9" rx="1.5"/><path d="M5 3V1.5h4V3"/></svg>Work</li>
    <li><svg width="14" height="14" viewBox="0 0 14 14" fill="none" stroke="#d7dbe4" stroke-width="1.2"><circle cx="7" cy="7" r="6"/><path d="M1 7h12M7 1c2 2 2 10 0 12M7 1c-2 2-2 10 0 12"/></svg>Social media</li>
    <li><svg width="14" height="14" viewBox="0 0 14 14" fill="none" stroke="#d7dbe4" stroke-width="1.2"><path d="M2 4h10l-.8 9H2.8z"/><path d="M4.5 4a2.5 2.5 0 015 0"/></svg>Shopping</li>
    <li><svg width="14" height="14" viewBox="0 0 14 14" fill="none" stroke="#d7dbe4" stroke-width="1.2"><path d="M13 1L1 6l5 2 2 5z"/><path d="M6 8l7-7"/></svg>Travel</li>
    <li><svg width="14" height="14" viewBox="0 0 14 14" fill="none" stroke="#d7dbe4" stroke-width="1.2"><path d="M1 5l6-3.5L13 5zM2 13h10M1 5h12M3 6v5M6 6v5M8 6v5M11 6v5"/></svg>Banking</li>
    <li><svg width="14" height="12" viewBox="0 0 14 12" fill="none" stroke="#d7dbe4" stroke-width="1.2"><rect x="1" y="1" width="12" height="10" rx="1.5"/><path d="M1.5 2l5.5 4.5L12.5 2"/></svg>Emails</li>
  </ul>
  <div class="side-divider"></div>
  <div class="plan">
    <div class="plan-art" role="img" aria-label="Illustration of a person riding a rocket"></div>
    <div class="plan-gem"><svg width="13" height="11" viewBox="0 0 13 11" fill="none" stroke="#c6cbd5" stroke-width="1"><path d="M1 4l2.5-3h6L12 4 6.5 10z"/><path d="M1 4h11M4.5 4l2 6 2-6M3.5 1l1 3M9.5 1l-1 3"/></svg></div>
    <div class="plan-label">Current Plan</div>
    <div class="plan-name">Trial Version Pro</div>
    <div class="plan-bar"><span></span></div>
    <div class="plan-day">Day 42 / 61</div>
    <div class="upgrade">Upgrade Plan</div>
  </div>
</nav>

<header class="topbar">
  <div class="search">
    <svg width="12" height="12" viewBox="0 0 12 12" fill="none" stroke="#b4c5e2" stroke-width="1.2"><circle cx="5.5" cy="5.5" r="4.5"/><path d="M9 9l2.5 2.5"/></svg>
    Search in Vault Keystone
    <svg class="filter" width="18" height="17" viewBox="0 0 18 17" fill="none" stroke="#b4c5e2" stroke-width="1.2"><path d="M4 1v15M14 1v15"/><circle cx="4" cy="11" r="2.5" fill="#f2f6fd"/><circle cx="14" cy="5" r="2.5" fill="#f2f6fd"/></svg>
  </div>
  <svg class="bell" width="14" height="16" viewBox="0 0 14 16" fill="none" stroke="#101318" stroke-width="1.3"><path d="M2 12V7a5 5 0 0110 0v5l1 1.2H1z"/><path d="M5.5 14.5a1.5 1.5 0 003 0"/></svg>
  <div class="me" role="img" aria-label="Profile photo"></div>
</header>

<h2 class="section-title" style="top:117px">Recently accessed</h2>

<div class="card c1" style="top:152px">
  <div class="tag"><i style="background:#fdeaf4"><svg width="8" height="8" viewBox="0 0 14 14" fill="none" stroke="#c95c9b" stroke-width="1.6"><path d="M13 1L1 6l5 2 2 5z"/></svg></i>Travel</div>
  <svg class="more" width="11" height="3" viewBox="0 0 11 3" fill="#101318"><circle cx="1.5" cy="1.5" r="1.3"/><circle cx="5.5" cy="1.5" r="1.3"/><circle cx="9.5" cy="1.5" r="1.3"/></svg>
  <h3>Bali Trip Itenary</h3><p>Last accessed : yesterday</p>
  <div class="avatars" role="img" aria-label="Shared with 2 members"><b style="background:#c4875b"></b><b style="background:#9d5fd0"></b></div>
</div>
<div class="card c2" style="top:152px">
  <div class="tag"><i style="background:#fdf1d4"><svg width="8" height="9" viewBox="0 0 14 15" fill="none" stroke="#c29b39" stroke-width="1.6"><path d="M8 1H3a2 2 0 00-2 2v9a2 2 0 002 2h3M8 1l4 4v2"/><circle cx="10" cy="11" r="2.5"/></svg></i>Encrypted file</div>
  <svg class="more" width="11" height="3" viewBox="0 0 11 3" fill="#101318"><circle cx="1.5" cy="1.5" r="1.3"/><circle cx="5.5" cy="1.5" r="1.3"/><circle cx="9.5" cy="1.5" r="1.3"/></svg>
  <h3>Finance Report May 2023</h3><p>Last accessed : July 20</p>
  <div class="avatars" role="img" aria-label="Shared with 12 members"><b style="background:#3c8a55"></b><b style="background:#e08a9a"></b><b style="background:#9d5fd0"></b><em>+9</em></div>
</div>
<div class="card c3" style="top:152px">
  <div class="tag"><i style="background:#e7eefc"><svg width="8" height="8" viewBox="0 0 14 14" fill="none" stroke="#2f64d6" stroke-width="1.6"><circle cx="7" cy="7" r="6"/><path d="M1 7h12M7 1c2 2 2 10 0 12M7 1c-2 2-2 10 0 12"/></svg></i>Social media</div>
  <svg class="more" width="11" height="3" viewBox="0 0 11 3" fill="#101318"><circle cx="1.5" cy="1.5" r="1.3"/><circle cx="5.5" cy="1.5" r="1.3"/><circle cx="9.5" cy="1.5" r="1.3"/></svg>
  <h3>Chatterly</h3><p>Last accessed : July 20</p>
  <div class="avatars" role="img" aria-label="Owner avatar"><b style="background:#c4875b"></b></div>
</div>
<div class="card c4" style="top:152px">
  <div class="tag"><i style="background:#fdf1d4"><svg width="8" height="9" viewBox="0 0 14 15" fill="none" stroke="#c29b39" stroke-width="1.6"><path d="M8 1H3a2 2 0 00-2 2v9a2 2 0 002 2h3M8 1l4 4v2"/><circle cx="10" cy="11" r="2.5"/></svg></i>Encrypted file</div>
  <svg class="more" width="11" height="3" viewBox="0 0 11 3" fill="#101318"><circle cx="1.5" cy="1.5" r="1.3"/><circle cx="5.5" cy="1.5" r="1.3"/><circle cx="9.5" cy="1.5" r="1.3"/></svg>
  <h3>Finance data 2023</h3><p>Last accessed : yesterday</p>
  <div class="avatars" role="img" aria-label="Shared with 2 members"><b style="background:#e08a9a"></b><b style="background:#9d5fd0"></b></div>
</div>

<h2 class="section-title" style="top:311px">My files</h2>
<div class="btn-new">New</div>
<div class="sort">Modified <svg width="10" height="6" viewBox="0 0 10 6" fill="none" stroke="#555b64" stroke-width="1.3"><path d="M1 1l4 4 4-4"/></svg></div>

<div class="folder green c1" style="top:345px"><div class="body"></div>
  <div class="ic"><svg width="15" height="13" viewBox="0 0 14 13" fill="none" stroke="#5aa570" stroke-width="1.2"><rect x="1" y="3" width="12" height="9" rx="1.5"/><path d="M5 3V1.5h4V3M1 7h12"/></svg></div>
  <div class="dots"><svg width="11" height="3" viewBox="0 0 11 3" fill="#101318"><circle cx="1.5" cy="1.5" r="1.3"/><circle cx="5.5" cy="1.5" r="1.3"/><circle cx="9.5" cy="1.5" r="1.3"/></svg></div>
  <h3>Work</h3><p>147 sources</p>
  <div class="avatars" role="img" aria-label="Shared with 12 members"><b style="background:#3c8a55"></b><b style="background:#e08a9a"></b><b style="background:#9d5fd0"></b><em style="background:#fff">+9</em></div>
</div>
<div class="folder yellow c2" style="top:345px"><div class="body"></div>
  <div class="ic"><svg width="13" height="14" viewBox="0 0 14 15" fill="none" stroke="#c29b39" stroke-width="1.2"><path d="M8 1H3a2 2 0 00-2 2v9a2 2 0 002 2h3M8 1l4 4v2"/><circle cx="10" cy="11" r="2.5"/></svg></div>
  <div class="dots"><svg width="11" height="3" viewBox="0 0 11 3" fill="#101318"><circle cx="1.5" cy="1.5" r="1.3"/><circle cx="5.5" cy="1.5" r="1.3"/><circle cx="9.5" cy="1.5" r="1.3"/></svg></div>
  <h3>Encrypted files</h3><p>14 sources</p>
  <div class="avatars" role="img" aria-label="Shared with 2 members"><b style="background:#3c8a55"></b><b style="background:#e08a9a"></b></div>
</div>
<div class="folder bluef c3" style="top:345px"><div class="body"></div>
  <div class="ic"><svg width="15" height="15" viewBox="0 0 14 14" fill="none" stroke="#2f64d6" stroke-width="1.2"><circle cx="7" cy="7" r="6"/><path d="M1 7h12M7 1c2 2 2 10 0 12M7 1c-2 2-2 10 0 12"/></svg></div>
  <div class="dots"><svg width="11" height="3" viewBox="0 0 11 3" fill="#101318"><circle cx="1.5" cy="1.5" r="1.3"/><circle cx="5.5" cy="1.5" r="1.3"/><circle cx="9.5" cy="1.5" r="1.3"/></svg></div>
  <h3>Social media</h3><p>8 sources</p>
</div>
<div class="folder red c4" style="top:345px"><div class="body"></div>
  <div class="ic"><svg width="13" height="13" viewBox="0 0 14 14" fill="none" stroke="#e2574c" stroke-width="1.3"><path d="M2 4h10l-.8 9H2.8z"/><path d="M4.5 4a2.5 2.5 0 015 0"/></svg></div>
  <div class="dots"><svg width="11" height="3" viewBox="0 0 11 3" fill="#101318"><circle cx="1.5" cy="1.5" r="1.3"/><circle cx="5.5" cy="1.5" r="1.3"/><circle cx="9.5" cy="1.5" r="1.3"/></svg></div>
  <h3>Shopping</h3><p>14 sources</p>
</div>

<div class="folder pink c1" style="top:474px"><div class="body"></div>
  <div class="ic"><svg width="13" height="13" viewBox="0 0 14 14" fill="none" stroke="#c95c9b" stroke-width="1.3"><path d="M13 1L1 6l5 2 2 5z"/><path d="M6 8l7-7"/></svg></div>
  <div class="dots"><svg width="11" height="3" viewBox="0 0 11 3" fill="#101318"><circle cx="1.5" cy="1.5" r="1.3"/><circle cx="5.5" cy="1.5" r="1.3"/><circle cx="9.5" cy="1.5" r="1.3"/></svg></div>
  <h3>Travel</h3><p>14 sources</p>
</div>
<div class="folder cyan c2" style="top:474px"><div class="body"></div>
  <div class="ic"><svg width="13" height="13" viewBox="0 0 14 14" fill="none" stroke="#5aa3b3" stroke-width="1.2"><path d="M1 5l6-3.5L13 5zM2 13h10M1 5h12M3 6v5M6 6v5M8 6v5M11 6v5"/></svg></div>
  <div class="dots"><svg width="11" height="3" viewBox="0 0 11 3" fill="#101318"><circle cx="1.5" cy="1.5" r="1.3"/><circle cx="5.5" cy="1.5" r="1.3"/><circle cx="9.5" cy="1.5" r="1.3"/></svg></div>
  <h3>Banking</h3><p>14 sources</p>
</div>
<div class="folder grey c3" style="top:474px"><div class="body"></div>
  <div class="ic"><svg width="13" height="13" viewBox="0 0 14 14" fill="none" stroke="#6b7079" stroke-width="1.2"><path d="M1 5l6-3.5L13 5zM2 13h10M1 5h12M3 6v5M6 6v5M8 6v5M11 6v5"/></svg></div>
  <div class="dots"><svg width="11" height="3" viewBox="0 0 11 3" fill="#101318"><circle cx="1.5" cy="1.5" r="1.3"/><circle cx="5.5" cy="1.5" r="1.3"/><circle cx="9.5" cy="1.5" r="1.3"/></svg></div>
  <h3>Email</h3><p>14 sources</p>
</div>
<div class="card c4" style="top:474px">
  <div class="tag"><i style="background:#fdf1d4"><svg width="8" height="9" viewBox="0 0 14 15" fill="none" stroke="#c29b39" stroke-width="1.6"><path d="M8 1H3a2 2 0 00-2 2v9a2 2 0 002 2h3M8 1l4 4v2"/><circle cx="10" cy="11" r="2.5"/></svg></i>Encrypted file</div>
  <svg class="more" width="11" height="3" viewBox="0 0 11 3" fill="#101318"><circle cx="1.5" cy="1.5" r="1.3"/><circle cx="5.5" cy="1.5" r="1.3"/><circle cx="9.5" cy="1.5" r="1.3"/></svg>
  <h3>Finance Report May 2023</h3><p>Last accessed : July 20</p>
  <div class="avatars" role="img" aria-label="Shared with 12 members"><b style="background:#3c8a55"></b><b style="background:#e08a9a"></b><b style="background:#9d5fd0"></b><em>+9</em></div>
</div>

<div class="card c1" style="top:602px">
  <div class="tag"><i style="background:#e7eefc"><svg width="8" height="8" viewBox="0 0 14 14" fill="none" stroke="#2f64d6" stroke-width="1.6"><circle cx="7" cy="7" r="6"/><path d="M1 7h12M7 1c2 2 2 10 0 12M7 1c-2 2-2 10 0 12"/></svg></i>Social media</div>
  <svg class="more" width="11" height="3" viewBox="0 0 11 3" fill="#101318"><circle cx="1.5" cy="1.5" r="1.3"/><circle cx="5.5" cy="1.5" r="1.3"/><circle cx="9.5" cy="1.5" r="1.3"/></svg>
  <h3>Chatterly</h3><p>Last accessed : July 20</p>
  <div class="avatars" role="img" aria-label="Owner avatar"><b style="background:#c4875b"></b></div>
</div>
<div class="card c2" style="top:602px">
  <div class="tag"><i style="background:#fdeaf4"><svg width="8" height="8" viewBox="0 0 14 14" fill="none" stroke="#c95c9b" stroke-width="1.6"><path d="M13 1L1 6l5 2 2 5z"/></svg></i>Travel</div>
  <svg class="more" width="11" height="3" viewBox="0 0 11 3" fill="#101318"><circle cx="1.5" cy="1.5" r="1.3"/><circle cx="5.5" cy="1.5" r="1.3"/><circle cx="9.5" cy="1.5" r="1.3"/></svg>
  <h3>Bali Trip Itenary</h3><p>Last accessed : yesterday</p>
  <div class="avatars" role="img" aria-label="Shared with 2 members"><b style="background:#c4875b"></b><b style="background:#9d5fd0"></b></div>
</div>
<div class="card c3" style="top:602px">
  <div class="tag"><i style="background:#e7eefc"><svg width="8" height="8" viewBox="0 0 14 14" fill="none" stroke="#2f64d6" stroke-width="1.6"><circle cx="7" cy="7" r="6"/><path d="M1 7h12M7 1c2 2 2 10 0 12M7 1c-2 2-2 10 0 12"/></svg></i>Social media</div>
  <svg class="more" width="11" height="3" viewBox="0 0 11 3" fill="#101318"><circle cx="1.5" cy="1.5" r="1.3"/><circle cx="5.5" cy="1.5" r="1.3"/><circle cx="9.5" cy="1.5" r="1.3"/></svg>
  <h3>Chatterly</h3><p>Last accessed : July 20</p>
  <div class="avatars" role="img" aria-label="Owner avatar"><b style="background:#c4875b"></b></div>
</div>

</body>
</html>
```